School Website

I need a design for a School (2 sections: Primary 6-12 years and Secondary 12-18 years). The first page is just a choice of the 2 sections. After we'll need 2 websites (with the same structure: Menu, ...) but with different colors. In fact, we need for end of October, 6 design of school website. So the best websites are going to be made available to you in the future (in pixmarketo) but privately.

Target Market(s)

Public, Parents, ...

Coding

Coded - Design and coding required

Number of Pages Required

5+ page

Font styles to use
Sans Serif

Colors
34a6d7
85cae6
cee9f5
ffffff

Requirements
Must have
• You can check the old Website: http: / /velmoq.be We need the same pages with the same content. Menu: - HomePage - News and communication (like blog page) - Activities (like blog page, with photo gallery) - Contact (Contact form + maps) - In the main menu, we need a special button to connect to an external Website ( button needs to be different than the other menu items The name of this button is "Parents Area"). The logo of 2 sections are attached. Please use it for the design and the choice of colors.
Nice to have
• This is a web design of other school that we like: https://www.quintel.be

```html
<!DOCTYPE html>
<html lang="en">
<head>
<meta charset="utf-8">
<title>Athénée Velmoq</title>
<link href="https://fonts.googleapis.com/css2?family=Montserrat:ital,wght@0,400;0,500;0,600;0,700;1,400&display=swap" rel="stylesheet">
<style>
:root{
  --navy:#0d4a86;
  --navy-deep:#0b2b52;
  --sky:#4cc8f2;
  --amber:#f5a91c;
  --ink:#223a5e;
  --text:#3b4552;
  --mist:#f3f3f3;
  --white:#ffffff;
}
*{margin:0;padding:0;box-sizing:border-box}
html,body{width:1200px;height:3688px;overflow:hidden}
body{position:relative;background:var(--white);font-family:'Montserrat',sans-serif;color:var(--text)}
.abs{position:absolute}
.brand{left:100px;top:30px;display:flex;align-items:center;gap:10px;font-size:24px;font-weight:700;color:var(--navy)}
.brand .mark{width:34px;height:34px;background:var(--sky);border-radius:50%}
.info{display:flex;gap:12px;font-size:11px;line-height:16px;color:#333}
.info svg{flex:none}
.nav{left:0;top:102px;width:1200px;height:51px;background:var(--navy)}
.nav ul{list-style:none}
.nav li{position:absolute;top:19px;font-size:11px;line-height:14px;color:var(--white);white-space:nowrap}
.parents{left:920px;top:93px;width:180px;height:69px}
.parents span{position:absolute;left:62px;top:28px;font-size:11px;font-weight:600;color:var(--navy)}
.hero{left:0;top:153px;width:1200px;height:630px;background:linear-gradient(120deg,#d9c6a4 0%,#e9e6dc 35%,#c99e78 62%,#b07a55 100%)}
.hero-box{left:0;top:590px;width:523px;height:193px;background:rgba(13,74,134,.78)}
.hero-box h1{position:absolute;left:97px;top:60px;font-size:36px;font-weight:600;line-height:38px;color:var(--white)}
.welcome h2{left:100px;top:880px;font-size:30px;line-height:37px;font-weight:600;color:var(--navy)}
.welcome p{left:353px;top:852px;width:750px;font-size:15px;line-height:30px;color:#2e4c70}
.feature-img{left:100px;top:1077px;width:500px;height:399px;background:linear-gradient(180deg,#b8a58c 0%,#d9cdb7 55%,#c8c5bf 100%)}
.feature{left:600px;top:1077px;width:500px;height:399px;background:var(--sky)}
.feature h3{position:absolute;left:90px;top:68px;font-size:31px;line-height:31px;font-weight:400;color:var(--navy)}
.feature h4{position:absolute;left:90px;top:140px;font-size:14px;font-weight:400;color:var(--white)}
.feature p{position:absolute;left:91px;top:172px;width:325px;font-size:10.5px;line-height:22.5px;color:#123a66}
.sec-title{width:1200px;left:0;text-align:center;font-size:24px;font-weight:700;color:var(--navy)}
.staff{width:156px;height:164px}
.link{font-size:14px;color:#222;text-decoration:underline}
.voices{left:0;top:2079px;width:1200px;height:467px;background:linear-gradient(180deg,rgba(11,43,82,.92),rgba(8,34,66,.97)),linear-gradient(90deg,#3c5a7a,#22405f)}
.quote{width:385px;font-size:11px;line-height:22.5px;color:var(--white)}
.qmark{font-size:60px;line-height:60px;color:rgba(255,255,255,.35);font-family:Georgia,serif}
.avatar{width:61px;height:61px;border-radius:50%;background:#c89a7e;border:2px solid var(--white)}
.person{font-size:11px;font-weight:600;color:var(--white)}
.dot{width:6px;height:6px;border-radius:50%;background:var(--white)}
.news{left:0;top:2546px;width:1200px;height:609px;background:var(--mist)}
.card{top:2714px;width:240px;height:326px;background:var(--white)}
.card .pic{height:159px}
.card h5{position:absolute;left:23px;top:177px;font-size:19px;font-weight:500;color:var(--navy)}
.card p{position:absolute;left:25px;top:210px;width:195px;font-size:9.5px;line-height:15px;color:#555}
.card .date{position:absolute;left:25px;top:283px;display:flex;gap:12px;font-size:10px;font-style:italic;color:#555}
.footer{left:0;top:3155px;width:1200px;height:399px;background:var(--navy);color:var(--white)}
.footer .flogo{position:absolute;left:100px;top:62px;display:flex;align-items:center;gap:10px;font-size:22px;font-weight:700}
.footer .flogo .mark{width:30px;height:30px;border-radius:50%;background:var(--sky)}
.footer h6{position:absolute;top:98px;font-size:14px;font-weight:600}
.footer .about-text{position:absolute;left:100px;top:150px;width:190px;font-size:11px;line-height:22.5px}
.fnews{position:absolute;left:354px;width:195px;font-size:9px;line-height:11px}
.fnews b{display:block;font-weight:600;margin-bottom:6px}
.fnews i{display:block;font-style:normal;font-size:8px;margin-top:6px}
.flinks{position:absolute;left:604px;top:150px;list-style:none;font-size:11px;line-height:22.7px}
.fcontact{position:absolute;left:858px;display:flex;gap:14px;font-size:11px;line-height:15px}
.social{top:3591px;width:26px;height:26px;border-radius:50%;background:#d9dde3}
.copy{left:0;top:3633px;width:1200px;text-align:center;font-size:8px;color:var(--navy)}
</style>
</head>
<body>

<header>
  <div class="abs brand"><span class="mark"></span>Athénée Velmoq</div>
  <div class="abs info" style="left:690px;top:36px">
    <svg width="12" height="16" viewBox="0 0 12 16"><path d="M6 0a6 6 0 0 1 6 6c0 4-6 10-6 10S0 10 0 6a6 6 0 0 1 6-6z" fill="#f5a91c"/><circle cx="6" cy="6" r="2.2" fill="#fff"/></svg>
    <div>Rue des Tilleuls 12 / B,<br>4520 Velmoq, Belgium</div>
  </div>
  <div class="abs info" style="left:943px;top:36px">
    <svg width="16" height="16" viewBox="0 0 16 16"><circle cx="8" cy="8" r="6.5" fill="none" stroke="#f5a91c" stroke-width="1.6"/><path d="M8 4v4.5l3 1.5" fill="none" stroke="#f5a91c" stroke-width="1.6"/></svg>
    <div>Monday to Friday<br>7 am - 6 pm</div>
  </div>
</header>

<nav class="abs nav">
  <ul>
    <li style="left:99px">HOME</li>
    <li style="left:155px">NEWS &amp; COMMUNICATION</li>
    <li style="left:325px">SCHEDULE &amp; DAYCARE</li>
    <li style="left:477px">PROCEDURE</li>
    <li style="left:573px">HOLIDAYS</li>
    <li style="left:650px">TEACHING STAFF</li>
    <li style="left:768px">ACTIVITIES</li>
    <li style="left:851px">CONTACT</li>
  </ul>
</nav>
<div class="abs parents">
  <svg width="180" height="69" viewBox="0 0 180 69"><polygon points="0,0 180,0 180,69 40,69" fill="#f5a91c"/></svg>
  <span>PARENTS AREA</span>
</div>

<section class="abs hero" role="img" aria-label="Photo of a smiling teacher leaning over a table with pupils in a classroom"></section>
<div class="abs hero-box"><h1>We ofer different<br>kinds of activities</h1></div>

<section class="welcome">
  <h2 class="abs">A WARM<br>WELCOME</h2>
  <p class="abs">Lorem ipsum dolor sit amet, consectetur adipiscing elit, sed do eiusmod tempor incididunt ut labore et dolore magna aliqua. Ut enim ad minim veniam, quis nostrud exercitation ullamco laboris nisi ut aliquip ex ea commodo consequat. Duis aute irure dolor in reprehenderit in voluptate velit esse cillum dolore eu fugiat nulla pariatur. Excepteur sint occaecat cupidatat non proident, sunt in culpa qui officia deserunt mollit anim id est laborum.</p>
</section>

<div class="abs feature-img" role="img" aria-label="Photo of schoolchildren with backpacks running outside the school"></div>
<section class="abs feature">
  <h3>Lorem ipsum dolor<br>sit amet</h3>
  <h4>Consectetur Adipiscing Elit</h4>
  <p>Lorem ipsum dolor sit amet, consectetur adipiscing elit, sed do eiusmod tempor incididunt ut labore et dolore magna aliqua. Ut enim ad minim veniam, quis nostrud exercitation ullamco laboris nisi ut aliquip ex ea commodo consequat. Duis aute irure dolor in reprehenderit in voluptate velit esse cillum dolore eu fugiat nulla pariatur.</p>
</section>

<h2 class="abs sec-title" style="top:1560px">OUR TEACHING STAFF</h2>
<div class="abs staff" style="left:100px;top:1625px;background:linear-gradient(135deg,#c7a27a,#8a6a55)" role="img" aria-label="Portrait of a teacher"></div>
<div class="abs staff" style="left:269px;top:1625px;background:linear-gradient(135deg,#eef0f3,#b4a6c9)" role="img" aria-label="Portrait of a teacher"></div>
<div class="abs staff" style="left:438px;top:1625px;background:linear-gradient(135deg,#f2f1ee,#c4a78a)" role="img" aria-label="Portrait of a teacher"></div>
<div class="abs staff" style="left:607px;top:1625px;background:linear-gradient(135deg,#e6e8ea,#d9c4b3)" role="img" aria-label="Portrait of a teacher"></div>
<div class="abs staff" style="left:775px;top:1625px;background:linear-gradient(135deg,#eeeeee,#2d3c63)" role="img" aria-label="Portrait of a teacher"></div>
<div class="abs staff" style="left:944px;top:1625px;background:linear-gradient(135deg,#8b6b4f,#e8e2da)" role="img" aria-label="Portrait of a teacher"></div>
<div class="abs staff" style="left:100px;top:1827px;background:linear-gradient(135deg,#9a7a5c,#ece8e3)" role="img" aria-label="Portrait of a teacher"></div>
<div class="abs staff" style="left:269px;top:1827px;background:linear-gradient(135deg,#b7c3d6,#b45a5a)" role="img" aria-label="Portrait of a teacher"></div>
<div class="abs staff" style="left:438px;top:1827px;background:linear-gradient(135deg,#c9ccd0,#f2f2f2)" role="img" aria-label="Portrait of a teacher"></div>
<div class="abs staff" style="left:607px;top:1827px;background:linear-gradient(135deg,#ebc8cb,#5a3b32)" role="img" aria-label="Portrait of a teacher"></div>
<span class="abs link" style="left:858px;top:1906px">View all Teachers</span>

<section class="abs voices" role="img" aria-label="Background photo of pupils playing in a schoolyard, darkened in navy">
  <div class="abs qmark" style="left:124px;top:80px">&ldquo;</div>
  <p class="abs quote" style="left:132px;top:101px">Lorem ipsum dolor sit amet consectetur adipiscing elit sed do eiusmod tempor incididunt ut labore et dolore magna aliqua. Ut enim ad minim veniam quis nostrud exercitation ullamco laboris nisi ut aliquip ex ea commodo consequat. Duis aute irure dolor in reprehenderit in voluptate velit esse cillum dolore eu fugiat nulla pariatur. Excepteur sint occaecat cupidatat non proident, sunt in culpa qui officia deserunt mollit anim id est laborum.</p>
  <div class="abs avatar" style="left:132px;top:277px" role="img" aria-label="Portrait of a parent"></div>
  <span class="abs person" style="left:215px;top:301px">Elena T. Marsh</span>

  <div class="abs qmark" style="left:631px;top:80px">&ldquo;</div>
  <p class="abs quote" style="left:639px;top:101px">Lorem ipsum dolor sit amet consectetur adipiscing elit sed do eiusmod tempor incididunt ut labore et dolore magna aliqua. Ut enim ad minim veniam quis nostrud exercitation ullamco laboris nisi ut aliquip ex ea commodo consequat. Duis aute irure dolor in reprehenderit in voluptate velit esse cillum dolore eu fugiat nulla pariatur. Excepteur sint occaecat cupidatat non proident, sunt in culpa qui officia deserunt mollit anim id est laborum.</p>
  <div class="abs avatar" style="left:639px;top:277px" role="img" aria-label="Portrait of a parent"></div>
  <span class="abs person" style="left:722px;top:301px">Nadia R. Colvin</span>

  <div class="abs dot" style="left:577px;top:385px;background:var(--sky)"></div>
  <div class="abs dot" style="left:596px;top:385px"></div>
  <div class="abs dot" style="left:614px;top:385px"></div>
</section>

<section class="abs news"></section>
<h2 class="abs sec-title" style="top:2624px">LATEST NEWS</h2>
<article class="abs card" style="left:97px">
  <div class="pic" style="background:linear-gradient(135deg,#d9b98f,#c23a3a)" role="img" aria-label="Photo of a teacher helping a pupil at a desk"></div>
  <h5>Lorem ipsum dolor</h5>
  <p>Lorem ipsum dolor sit amet consectetur adipiscing elit sed do eiusmod tempor incididunt ut labore et dolore magna aliqua.</p>
  <div class="date"><svg width="12" height="12" viewBox="0 0 12 12"><rect x="1" y="2" width="10" height="9" fill="none" stroke="#4cc8f2"/><path d="M1 5h10M4 0v3M8 0v3" stroke="#4cc8f2"/></svg>2 days ago</div>
</article>
<article class="abs card" style="left:354px">
  <div class="pic" style="background:linear-gradient(135deg,#e8e4dc,#2f3b55)" role="img" aria-label="Photo of pupils writing in a classroom"></div>
  <h5>Lorem ipsum dolor</h5>
  <p>Lorem ipsum dolor sit amet consectetur adipiscing elit sed do eiusmod tempor incididunt ut labore et dolore magna aliqua.</p>
  <div class="date"><svg width="12" height="12" viewBox="0 0 12 12"><rect x="1" y="2" width="10" height="9" fill="none" stroke="#4cc8f2"/><path d="M1 5h10M4 0v3M8 0v3" stroke="#4cc8f2"/></svg>2 days ago</div>
</article>
<article class="abs card" style="left:607px">
  <div class="pic" style="background:linear-gradient(135deg,#cfd2cc,#7a6a58)" role="img" aria-label="Photo of children sitting on the floor listening to a teacher"></div>
  <h5>Lorem ipsum dolor</h5>
  <p>Lorem ipsum dolor sit amet consectetur adipiscing elit sed do eiusmod tempor incididunt ut labore et dolore magna aliqua.</p>
  <div class="date"><svg width="12" height="12" viewBox="0 0 12 12"><rect x="1" y="2" width="10" height="9" fill="none" stroke="#4cc8f2"/><path d="M1 5h10M4 0v3M8 0v3" stroke="#4cc8f2"/></svg>2 days ago</div>
</article>
<article class="abs card" style="left:859px">
  <div class="pic" style="background:linear-gradient(135deg,#f0d7b2,#3f8fd0)" role="img" aria-label="Photo of smiling children at a table with pencils"></div>
  <h5>Lorem ipsum dolor</h5>
  <p>Lorem ipsum dolor sit amet consectetur adipiscing elit sed do eiusmod tempor incididunt ut labore et dolore magna aliqua.</p>
  <div class="date"><svg width="12" height="12" viewBox="0 0 12 12"><rect x="1" y="2" width="10" height="9" fill="none" stroke="#4cc8f2"/><path d="M1 5h10M4 0v3M8 0v3" stroke="#4cc8f2"/></svg>2 days ago</div>
</article>
<span class="abs link" style="left:551px;top:3078px">View all News</span>

<footer class="abs footer">
  <div class="flogo"><span class="mark"></span>Athénée Velmoq</div>
  <p class="about-text">Lorem ipsum dolor sit amet consectetur adipiscing elit sed do eiusmod tempor incididunt ut labore et dolore magna aliqua. Ut enim ad minim veniam quis nostrud exercitation ullamco.</p>

  <h6 style="left:354px">Latest News</h6>
  <div class="fnews" style="top:152px"><b>Lorem ipsum dolor</b>Lorem ipsum dolor sit amet consectetur adipiscing elit sed do<i>Sept 30, 2019</i></div>
  <svg class="abs" style="left:354px;top:231px" width="195" height="1"><rect width="195" height="1" fill="rgba(255,255,255,.35)"/></svg>
  <div class="fnews" style="top:246px"><b>Lorem ipsum dolor</b>Lorem ipsum dolor sit amet consectetur adipiscing elit sed do<i>Sept 30, 2019</i></div>

  <h6 style="left:604px">About</h6>
  <ul class="flinks"><li>Home</li><li>News &amp; Communication</li><li>Schedule &amp; Daycare</li><li>Procedure</li><li>Holidays</li><li>Teaching Staff</li><li>Activities</li><li>Contact</li></ul>

  <h6 style="left:858px">Contact</h6>
  <div class="fcontact" style="top:156px"><svg width="11" height="14" viewBox="0 0 12 16"><path d="M6 0a6 6 0 0 1 6 6c0 4-6 10-6 10S0 10 0 6a6 6 0 0 1 6-6z" fill="#f5a91c"/><circle cx="6" cy="6" r="2.2" fill="#0d4a86"/></svg><span>Rue des Tilleuls 12 / B,<br>4520 Velmoq, Belgium</span></div>
  <div class="fcontact" style="top:210px"><svg width="12" height="12" viewBox="0 0 12 12"><path d="M2 0l3 3-1.5 2a8 8 0 0 0 3.5 3.5L9 7l3 3-2 2C5 12 0 7 0 2z" fill="#f5a91c"/></svg><span>321 654 9870</span></div>
  <div class="fcontact" style="top:244px"><svg width="12" height="10" viewBox="0 0 12 10"><rect width="12" height="10" fill="#f5a91c"/><path d="M0 0l6 5 6-5" fill="none" stroke="#0d4a86"/></svg><span>info@atheneevelmoq.com</span></div>
</footer>

<div class="abs social" style="left:526px"></div>
<div class="abs social" style="left:566px"></div>
<div class="abs social" style="left:606px"></div>
<div class="abs social" style="left:645px"></div>
<p class="abs copy">© 2019. All Rights Reserved. Privacy Policy</p>

</body>
</html>
```